Business Card Design Project

Actor, Producer, Vocal Coach, Choral Director, Song WriterPhone: (215) 555-0142 Fax: (215) 856-3933Email: waltierblocker@gmail.comFacebook: facebook.com/waltier.blockerTwitter: @thedf907

Industry/Entity Type

Business

Contact Information for Business Card

Business Cards that include my picture

Colors

Designer to choose colors to be used in the design.

```html
<!DOCTYPE html>
<html lang="en">
<head>
<meta charset="utf-8">
<title>Marlon Pryce — Business Card</title>
<link href="https://fonts.googleapis.com/css2?family=Open+Sans:wght@400;600&display=swap" rel="stylesheet">
<style>
  :root {
    --backdrop: #e7e3de;
    --card-black: #0b0b0c;
    --card-grey: #2a2a2d;
    --pink: #e2588f;
    --pink-soft: #ec94bd;
    --pink-deep: #b8406f;
    --text-light: #f1f1f1;
  }
  * { box-sizing: border-box; margin: 0; padding: 0; }
  html, body { width: 1200px; height: 1023px; overflow: hidden; }
  body {
    background: var(--backdrop);
    font-family: "Open Sans", Arial, sans-serif;
    position: relative;
  }
  .card {
    position: absolute;
    left: 320px;
    width: 560px;
    height: 320px;
    border-radius: 18px;
    overflow: hidden;
    background: linear-gradient(135deg, var(--card-grey) 0%, var(--card-black) 55%, var(--card-black) 100%);
    box-shadow: 0 14px 34px rgba(0,0,0,0.28);
  }
  .card--front { top: 150px; }
  .card--back { top: 553px; }

  /* front */
  .front-band {
    position: absolute;
    left: 170px; top: 0;
    width: 170px; height: 100%;
    background: linear-gradient(180deg, var(--pink-soft) 0%, var(--pink) 100%);
  }
  .portrait-ring {
    position: absolute;
    left: 150px; top: 40px;
    width: 210px; height: 170px;
    border-radius: 50%;
    border: 3px solid var(--pink);
    background: var(--card-black);
    padding: 5px;
  }
  .portrait {
    width: 100%; height: 100%;
    border-radius: 50%;
    background: radial-gradient(ellipse at 45% 55%, #ffffff 0%, #ececec 55%, #7a5a48 100%);
  }

  /* back */
  .back-stripe {
    position: absolute;
    left: 0; top: 0;
    width: 34px; height: 100%;
    background: linear-gradient(180deg, var(--pink) 0%, var(--pink-deep) 100%);
  }
  .identity {
    position: absolute;
    right: 36px; top: 34px;
    text-align: right;
  }
  .identity__name {
    color: var(--pink);
    font-size: 30px;
    font-weight: 600;
    line-height: 1.1;
  }
  .identity__roles {
    color: var(--text-light);
    font-size: 15px;
    line-height: 1.4;
    margin-top: 6px;
  }
  .contacts {
    position: absolute;
    right: 36px; bottom: 30px;
    list-style: none;
  }
  .contacts__item {
    display: flex;
    justify-content: flex-end;
    align-items: center;
    gap: 10px;
    color: var(--text-light);
    font-size: 14px;
    line-height: 24px;
    white-space: nowrap;
  }
  .contacts__icon { width: 13px; height: 13px; flex: none; }
  .contacts__dot {
    width: 9px; height: 9px; border-radius: 50%;
    background: var(--pink); flex: none; margin: 0 2px;
  }
</style>
</head>
<body>

<section class="card card--front" aria-label="Card front">
  <div class="front-band"></div>
  <div class="portrait-ring">
    <div class="portrait" role="img" aria-label="Portrait photo of the performer in a white shirt and pink tie"></div>
  </div>
</section>

<section class="card card--back" aria-label="Card back">
  <div class="back-stripe"></div>
  <div class="identity">
    <h1 class="identity__name">Marlon Pryce</h1>
    <p class="identity__roles">Actor, Producer, Vocal Coach,<br>Choral Director, Song Writer</p>
  </div>
  <ul class="contacts">
    <li class="contacts__item">(215) 555-0142
      <svg class="contacts__icon" viewBox="0 0 16 16"><path fill="#e2588f" d="M3.6 1.2l2.2 2.6-1.3 1.6c.9 2.2 2.6 3.9 4.8 4.8l1.6-1.3 2.6 2.2-1.2 2.2C7.4 14.8 1.2 8.6 1.4 2.4z"/></svg>
    </li>
    <li class="contacts__item">(215) 555-0178 <span class="contacts__dot"></span></li>
    <li class="contacts__item">dorianfenwick@mailbox.example
      <svg class="contacts__icon" viewBox="0 0 16 16"><rect x="1.5" y="3.5" width="13" height="9" fill="none" stroke="#e2588f" stroke-width="1.5"/><path d="M1.5 3.5L8 9l6.5-5.5" fill="none" stroke="#e2588f" stroke-width="1.5"/></svg>
    </li>
    <li class="contacts__item">fanpage.example/dorian.fenwick <span class="contacts__dot"></span></li>
    <li class="contacts__item">@thedf907 <span class="contacts__dot"></span></li>
  </ul>
</section>

</body>
</html>
```